ultra-minimalist business card

front (black background, matte):

tarik b. hosseny
writer | photographer
get@tarikhosseny.com

back (white background, matte):

a picture speaks a thousand words;
a word draws a thousand pictures.

www.tarikhosseny.com

all text should be small (white or silver - as long as it shows against the black - on the front; black or gray - as long as it shows against the white - on the back).

feel free to get creative in terms of arrangement, alignment, and font type, but remember, the overall style is minimalist, so nothing too fancy, please.

thanks.

```html
<!DOCTYPE html>
<html lang="en">
<head>
<meta charset="utf-8">
<title>tarik b. hosseny — business card</title>
<link rel="stylesheet" href="https://fonts.googleapis.com/css2?family=Montserrat:ital,wght@0,300;0,400;0,600;1,300&display=swap">
<style>
  :root {
    --bg: #d6d7d9;
    --card-black: #232323;
    --card-white: #f2f2f1;
    --accent: #8cc2e6;
    --front-name: #f4f4f4;
    --front-muted: #b9b9b9;
    --back-quote: #4a4a4a;
    --back-url: #2e2e2e;
  }
  * { margin: 0; padding: 0; box-sizing: border-box; }
  html, body {
    width: 1200px;
    height: 900px;
    overflow: hidden;
    background: var(--bg);
    font-family: "Montserrat", sans-serif;
  }
  .sheet {
    width: 1200px;
    height: 900px;
    display: flex;
    flex-direction: column;
    align-items: center;
    justify-content: center;
    gap: 44px;
  }
  .card {
    position: relative;
    width: 560px;
    height: 320px;
    box-shadow: 0 6px 18px rgba(0,0,0,0.12);
  }
  .card--front { background: var(--card-black); }
  .card--back { background: var(--card-white); }

  .identity {
    position: absolute;
    left: 44px;
    bottom: 44px;
    display: flex;
    align-items: stretch;
    gap: 14px;
  }
  .identity__bar {
    width: 5px;
    background: var(--accent);
  }
  .identity__name {
    font-weight: 600;
    font-size: 19px;
    color: var(--front-name);
    line-height: 1.15;
  }
  .identity__role {
    font-weight: 300;
    font-size: 14px;
    color: var(--front-muted);
    line-height: 1.3;
  }
  .contact {
    position: absolute;
    right: 44px;
    bottom: 46px;
    display: flex;
    align-items: center;
    gap: 14px;
    font-weight: 400;
    font-size: 13px;
    color: var(--front-muted);
  }
  .tick {
    display: inline-block;
    width: 3px;
    height: 12px;
    background: var(--accent);
  }

  .quote {
    position: absolute;
    right: 44px;
    bottom: 92px;
    text-align: right;
    font-style: italic;
    font-weight: 300;
    font-size: 20px;
    line-height: 1.25;
    color: var(--back-quote);
  }
  .website {
    position: absolute;
    right: 44px;
    bottom: 50px;
    display: flex;
    align-items: center;
    gap: 14px;
    font-weight: 400;
    font-size: 13px;
    color: var(--back-url);
  }
</style>
</head>
<body>
  <main class="sheet">
    <section class="card card--front" aria-label="card front">
      <div class="identity">
        <span class="identity__bar"></span>
        <div class="identity__text">
          <p class="identity__name">tarik b. hosseny</p>
          <p class="identity__role">writer/photographer</p>
        </div>
      </div>
      <p class="contact">get@tarikhosseny.com <span class="tick"></span></p>
    </section>

    <section class="card card--back" aria-label="card back">
      <p class="quote">a picture speaks a thousand words;<br>a word draws a thousand pictures.</p>
      <p class="website">www.tarikhosseny.com <span class="tick"></span></p>
    </section>
  </main>
</body>
</html>
```